Medical Practice Business Card

we need a business card for our new medical ophthalmology practice based in Needham Massachusetts. we are looking for a simple , modern and elegant design.
the card needs to contain the following
1- the logo of our practice (please see attached file)
2- the name of the practice : "Silver Birch Retina Care"
3- Doctor's Name: Tobias Rendell MD PhD
4- Specialty: Board-Certified Vitreoretinal Surgeon
5- practice address: 87 Larkspur Ave, Suite 210, Needham MA 02481
7- Office number: 617- 482 - 7730
8- fax number: 617- 391 - 2268
9- email: info@sbretinahub.example
10- website: www.sbretinahub.example

```html
<!DOCTYPE html>
<html lang="en">
<head>
<meta charset="utf-8">
<title>Silver Birch Retina Care – Business Card</title>
<link rel="stylesheet" href="https://fonts.googleapis.com/css2?family=Cinzel:wght@700&family=Poppins:wght@400&display=swap">
<style>
  :root {
    --page-bg: #c4c4c4;
    --navy: #1a395c;
    --royal: #0a4fa6;
    --sky: #7fd9e6;
    --mid-blue: #3a86d0;
    --ink: #1b1b1b;
    --paper: #ffffff;
  }
  * { margin: 0; padding: 0; box-sizing: border-box; }
  html, body { width: 1093px; height: 1200px; overflow: hidden; }
  body {
    background: var(--page-bg);
    position: relative;
    font-family: "Poppins", sans-serif;
    color: var(--ink);
  }
  .card {
    position: absolute;
    left: 265px;
    width: 578px;
    height: 357px;
    border-radius: 28px;
    overflow: hidden;
  }
  .card-front { top: 226px; background: var(--paper); }
  .card-back { top: 621px; background: var(--navy); }

  .side-band { position: absolute; left: 0; top: 0; width: 90px; height: 100%; }

  .doctor-name {
    position: absolute; left: 79px; top: 122px;
    font-family: "Cinzel", serif; font-weight: 700;
    font-size: 18px; color: var(--navy); letter-spacing: 0.2px;
  }
  .specialty {
    position: absolute; left: 79px; top: 145px;
    font-size: 16.5px; color: #2a2a2a;
  }
  .rule {
    position: absolute; left: 79px; right: 0; top: 182px; height: 3px;
    background: linear-gradient(90deg, var(--sky), #2f7fc7 60%, var(--royal));
  }
  .contact-list { position: absolute; left: 79px; top: 200px; list-style: none; }
  .contact-list li {
    display: flex; align-items: center; gap: 5px;
    font-size: 16.5px; line-height: 21px; height: 21px;
  }
  .contact-list svg { width: 16px; height: 16px; fill: var(--navy); flex: none; }
  .web-host { color: var(--navy); }

  .address {
    position: absolute; right: 30px; top: 235px;
    text-align: right; font-size: 16.5px; line-height: 21px;
    font-style: normal;
  }

  .practice-name {
    position: absolute; left: 0; right: 0; top: 50%;
    transform: translateY(-50%);
    text-align: center;
    font-family: "Poppins", sans-serif; font-weight: 400;
    font-size: 28px; line-height: 40px; color: var(--mid-blue);
  }
</style>
</head>
<body>
  <section class="card card-front" aria-label="Business card front">
    <svg class="side-band" viewBox="0 0 90 357" preserveAspectRatio="none" aria-hidden="true">
      <path d="M0 0 H70 Q20 178 70 357 H0 Z" fill="var(--navy)"/>
    </svg>

    <h1 class="doctor-name">Tobias Rendell MD PhD</h1>
    <p class="specialty">Board-Certified Vitreoretinal Surgeon</p>
    <div class="rule" aria-hidden="true"></div>

    <ul class="contact-list">
      <li>
        <svg viewBox="0 0 24 24" aria-hidden="true"><path d="M6.6 10.8a15.1 15.1 0 0 0 6.6 6.6l2.2-2.2a1 1 0 0 1 1-.25 11.4 11.4 0 0 0 3.6.57 1 1 0 0 1 1 1V20a1 1 0 0 1-1 1A17 17 0 0 1 3 4a1 1 0 0 1 1-1h3.5a1 1 0 0 1 1 1c0 1.25.2 2.45.57 3.57a1 1 0 0 1-.25 1z"/></svg>
        617- 482 - 7730
      </li>
      <li>
        <svg viewBox="0 0 24 24" aria-hidden="true"><path d="M6 2h12v5H6zM3 8h18a2 2 0 0 1 2 2v7h-4v5H5v-5H1v-7a2 2 0 0 1 2-2zm4 8v4h10v-4z"/></svg>
        617- 391 - 2268
      </li>
      <li>
        <svg viewBox="0 0 24 24" aria-hidden="true"><path d="M2 5h20v14H2zm2 2v.5l8 5.5 8-5.5V7l-8 5.5z"/></svg>
        info@sbretinahub.example
      </li>
      <li>
        <svg viewBox="0 0 24 24" aria-hidden="true"><path d="M12 2a10 10 0 1 0 0 20 10 10 0 0 0 0-20zm6.9 6h-3a15 15 0 0 0-1.3-4 8 8 0 0 1 4.3 4zM12 4.1c.8 1.1 1.5 2.4 1.9 3.9h-3.8c.4-1.5 1.1-2.8 1.9-3.9zM4.3 14a8 8 0 0 1 0-4h3.4a16 16 0 0 0 0 4zm.8 2h3a15 15 0 0 0 1.3 4 8 8 0 0 1-4.3-4zm3-8h-3a8 8 0 0 1 4.3-4 15 15 0 0 0-1.3 4zM12 19.9c-.8-1.1-1.5-2.4-1.9-3.9h3.8c-.4 1.5-1.1 2.8-1.9 3.9zm2.3-5.9H9.7a14 14 0 0 1 0-4h4.6a14 14 0 0 1 0 4zm.3 5.9a15 15 0 0 0 1.3-3.9h3a8 8 0 0 1-4.3 3.9zm1.7-5.9a16 16 0 0 0 0-4h3.4a8 8 0 0 1 0 4z"/></svg>
        <span>www.<span class="web-host">sbretinahub</span>.example</span>
      </li>
    </ul>

    <address class="address">
      87 Larkspur Ave, Suite 210<br>
      Needham MA 02481
    </address>
  </section>

  <section class="card card-back" aria-label="Business card back">
    <p class="practice-name">Silver Birch Retina Care</p>
  </section>
</body>
</html>
```